Brochure Design Project

I require a brochure with inserts inside that show our different services for different industries.

The insides of the brochure will have "about our company" ie, trackered vans - pda's and software used - images of the team and showing we invest in the very latest equipment and softwares to offer the best highest quality service. etc etc then the inserts demonstrating what we can do for each industry - images working on sites, equipment used etc etc on the back of each sheet a case study proving implementation.

Construction
Public Transport
Hotel & Leisure
Retail / Businesses
Housing Association

The inserts I imagine will be different in size or cut differently down the sides in order to allow the reader to see the different sectors and go to the one they require. The brochure will go in full to some companies - like facilities management whom would be interested in all the work we do for industries - however the brochure may contain just one of the inserts if we visit say a construction site in which they would only be interested in one (construction)

The inserts will show all the services we offer for that industry and maybe to the rear have a case study in which proves our implementation of service.

Our overall company is to offer solutions for damaged , worn or complete change of style to surfaces. For example we offer invisible damage repairs to surfaces like woods, laminates, ceramics etc.
We offer full scale resurfacing from bath re-enamelling to commercial spraying of powdercoating, metal work on offices.

also must have slot for business card.

Our communication to the customer is that using our services you can repair or resurface items back to new at the fraction of the cost of replacement thus reducing landfil as you are replacing not repairing. You get the brand new finish for a lot less cost - time and mess.

VELTIQ - cutting cost with the environment in mind.

Target Market(s)

Various sectors as indicated. Business card slot.

Industry/Entity Type

Communication

Requirements
Must have
• inserts cut down the side in a way that looks good when one single insert is added but all look great showing through each sector when all added together.

```html
<!DOCTYPE html>
<html lang="en">
<head>
<meta charset="utf-8">
<title>VELTIQ – Company Brochure</title>
<link rel="stylesheet" href="https://fonts.googleapis.com/css2?family=Tenor+Sans&family=Questrial&family=Open+Sans:ital,wght@0,400;1,300&display=swap">
<style>
  :root {
    --ink: #111111;
    --green: #8dc63f;
    --grey-light: #f6f6f6;
    --grey-mid: #dcdcdd;
    --grey-dark: #c2c3c5;
    --white: #ffffff;
    --tab-line: #9a9a9a;
    --crop: #e6007e;
  }
  * { box-sizing: border-box; margin: 0; padding: 0; }
  html, body { width: 848px; height: 1200px; overflow: hidden; background: var(--white); }
  .brochure { position: relative; width: 848px; height: 1200px; overflow: hidden; background: var(--white); }

  .cover {
    position: absolute; left: 0; top: 0; width: 798px; height: 1200px;
    background: linear-gradient(90deg, var(--grey-light) 0%, var(--grey-mid) 55%, var(--grey-dark) 100%);
  }

  .brand-dot {
    position: absolute; left: 352px; top: 140px; width: 150px; height: 150px;
    border-radius: 50%; background: var(--green);
  }
  .brand-name {
    position: absolute; left: 0; width: 798px; top: 375px; text-align: center;
    font-family: "Tenor Sans", sans-serif; font-size: 100px; line-height: 1;
    color: var(--ink); letter-spacing: 4px;
  }
  .tagline {
    position: absolute; left: 0; width: 798px; top: 570px; text-align: center;
    font-family: "Tenor Sans", sans-serif; font-size: 28px; letter-spacing: 2.5px;
    color: var(--green);
  }
  .tagline .sep { color: var(--ink); margin: 0 6px; }
  .strapline {
    position: absolute; left: 0; width: 798px; top: 650px; text-align: center;
    font-family: "Questrial", sans-serif; font-size: 21px; color: var(--ink);
  }
  .strapline em { font-style: normal; color: var(--green); }

  .card-slot { position: absolute; left: 225px; top: 800px; width: 400px; height: 290px; }

  .doc-title {
    position: absolute; left: 728px; top: 1182px; transform-origin: 0 0; transform: rotate(-90deg);
    font-family: "Open Sans", sans-serif; font-style: italic; font-weight: 300;
    font-size: 50px; color: var(--white); white-space: nowrap; letter-spacing: 1px;
  }

  .sector-tabs { position: absolute; left: 798px; top: 0; width: 50px; height: 1200px; }
  .tab {
    position: absolute; left: 0; width: 50px;
    border-radius: 0 22px 22px 0;
    display: flex; align-items: center; justify-content: center;
    border: 1px solid var(--tab-line); border-left: none;
  }
  .tab span {
    writing-mode: vertical-rl;
    font-family: "Open Sans", sans-serif; font-size: 11px; white-space: nowrap;
  }
  .tab--green { background: var(--green); border-color: var(--green); color: var(--ink); }
  .tab--white { background: var(--white); color: var(--ink); }
  .tab--black { background: var(--ink); border-color: var(--ink); color: var(--white); }
  .tab--construction { top: 46px; height: 171px; }
  .tab--transport { top: 217px; height: 146px; }
  .tab--hotel { top: 363px; height: 171px; }
  .tab--retail { top: 534px; height: 171px; }
  .tab--housing { top: 705px; height: 157px; }
</style>
</head>
<body>
<main class="brochure">
  <section class="cover">
    <div class="brand-dot"></div>
    <h1 class="brand-name">VELTIQ</h1>
    <p class="tagline">REPAIR<span class="sep">•</span>RESTORE<span class="sep">•</span>RESURFACE</p>
    <p class="strapline">Cutting cost with <em>the environment</em> in mind</p>

    <svg class="card-slot" viewBox="0 0 400 290" aria-label="Business card slot">
      <rect x="19" y="24" width="362" height="238" fill="none" stroke="#ffffff" stroke-width="1.5"/>
      <line x1="346" y1="9" x2="391" y2="56" stroke="#e6007e" stroke-width="1.5"/>
      <line x1="7" y1="226" x2="51" y2="275" stroke="#e6007e" stroke-width="1.5"/>
    </svg>

    <p class="doc-title">Company Brochure</p>
  </section>

  <nav class="sector-tabs">
    <div class="tab tab--green tab--construction"><span>Construction</span></div>
    <div class="tab tab--white tab--transport"><span>Public Transport</span></div>
    <div class="tab tab--black tab--hotel"><span>Hotel &amp; Leisure</span></div>
    <div class="tab tab--green tab--retail"><span>Retail/Businesses</span></div>
    <div class="tab tab--white tab--housing"><span>Housing Association</span></div>
  </nav>
</main>
</body>
</html>
```